Brand new letterhead, business card, email signature etc.

We are a financial company in London, UK. Our website is www.quorvane.com. We're wanting a complete remodel of the company colours, letter head, business cards, email signatures, etc. Looking to keep the same font for the company name. I have upload a colour palette that we want to work with. We're looking for company letterhead for outgoing letters/ correspondence, letterhead for internal documentation, email signatures, e-letters. etc. Ultimately we will redesign the entire website also. It is important that our clients get a strong, secure, warm, trustworthy, solid feeling and first impression.
Updates

Designs look the same

Target Market(s)

Institutional investors, (ultra) high net worth individuals

Industry/Entity Type

Finance, Invesments banking.

Font styles to use
Other font styles liked:
• Current font is "Champagne & Limousines"

Requirements
Must have
• Must use the colours provided on the PDF uploaded to the portal. The purple = main colour. The red = accent colour.
Nice to have
• Nice to use same font as now for the company name "Marlowin". Font is "Champagne & Limousines". Nice to have some reference to the old logo flower, but only subtle.
Should not have
• Do not use the colour red from our website. Use the colours provided on the colour palette PDF that I uploaded in the portal.

```html
<!DOCTYPE html>
<html lang="en">
<head>
<meta charset="utf-8">
<title>Marlowin Letterhead</title>
<link rel="stylesheet" href="https://fonts.googleapis.com/css2?family=Inter:wght@300;400&display=swap">
<style>
  :root {
    --backdrop: #a4aba7;
    --paper: #f0f0f0;
    --ink: #2a2a2a;
    --body-text: #6e6e6e;
    --accent: #c8201e;
    --placeholder: #e2e2e2;
  }
  * { margin: 0; padding: 0; box-sizing: border-box; }
  html, body {
    width: 1200px; height: 803px; overflow: hidden;
    background: var(--backdrop);
    font-family: "Inter", Arial, sans-serif;
  }
  .letterhead {
    position: absolute; left: 331px; top: 21px;
    width: 538px; height: 762px;
    background: var(--paper);
  }
  .brand {
    position: absolute; left: 51px; top: 42px;
    display: flex; align-items: center; gap: 9px;
  }
  .brand-square {
    width: 44px; height: 44px;
    border: 1px solid var(--ink);
  }
  .brand-name {
    font-weight: 300; font-size: 22px; letter-spacing: 3px;
    color: var(--ink); text-transform: uppercase;
  }
  .address {
    position: absolute; left: 306px; top: 51px;
    font-size: 7.4px; line-height: 10px; color: var(--ink); font-weight: 300;
  }
  .divider {
    position: absolute; left: 390px; top: 52px;
    width: 1px; height: 26px; background: var(--accent);
  }
  .contact {
    position: absolute; left: 396px; top: 51px;
    list-style: none; font-size: 7.4px; line-height: 10px;
    color: var(--ink); font-weight: 300;
  }
  .contact li { display: flex; align-items: center; gap: 4px; }
  .contact svg { width: 6px; height: 6px; fill: var(--accent); flex: none; }
  .date {
    position: absolute; right: 53px; top: 187px;
    font-size: 10.2px; color: var(--body-text); font-weight: 300;
  }
  .letter-body {
    position: absolute; left: 46px; top: 213px; width: 439px;
    font-size: 10.1px; line-height: 15.2px; color: var(--body-text); font-weight: 300;
  }
  .salutation { margin-bottom: 12px; }
  .letter-body p.paragraph { text-align: justify; margin-bottom: 21px; }
  .signature {
    position: absolute; left: 44px; top: 576px;
    width: 96px; height: 60px; background: var(--placeholder);
  }
</style>
</head>
<body>
  <main class="letterhead">
    <header>
      <div class="brand">
        <div class="brand-square"></div>
        <span class="brand-name">Marlowin</span>
      </div>
      <address class="address">
        Suite 42/1880<br>Harrowden Park Lane<br>Elmbrook VIC 3175
      </address>
      <div class="divider"></div>
      <ul class="contact">
        <li><svg viewBox="0 0 10 10"><path d="M2 0.5 L3.6 2.8 L2.7 3.8 Q4 6.2 6.2 7.3 L7.2 6.4 L9.5 8 L8.3 9.5 Q1 8 0.5 1.7 Z"/></svg>1870 34 62 18</li>
        <li><svg viewBox="0 0 10 10"><path d="M0 2 H10 V8.5 H0 Z M0.6 2.4 L5 5.6 L9.4 2.4" stroke="#f0f0f0" stroke-width="0.8"/></svg>contact@quorvane.com</li>
        <li><svg viewBox="0 0 10 10"><circle cx="5" cy="5" r="4.5"/></svg>quorvane.com</li>
      </ul>
    </header>

    <p class="date">Dated: February 15, 2023</p>

    <section class="letter-body">
      <p class="salutation">Dear Sir,</p>
      <p class="paragraph">Lorem Ipsum is simply dummy text of the printing and typesetting industry. Lorem Ipsum has been the industry's standard dummy text ever since the 1500s, when an unknown printer took a galley of type and scrambled it to make a type specimen book. It has survived not only five centuries, but also the leap into electronic typesetting, remaining essentially unchanged. It was popularised in the 1960s with the release of Transfertype sheets containing Lorem Ipsum passages, and more recently with desktop publishing software like Folio LayoutDesk including versions of Lorem Ipsum.</p>
      <p class="paragraph">It is a long established fact that a reader will be distracted by the readable content of a page when looking at its layout. The point of using Lorem Ipsum is that it has a more-or-less normal distribution of letters, as opposed to using 'Content here, content here', making it look like readable English. Many desktop publishing packages and web page editors now use Lorem Ipsum as their default model text, and a search for 'lorem ipsum' will uncover many web sites still in their infancy. Various versions have evolved over the years, sometimes by accident, sometimes on purpose (injected humour and the like).</p>
      <p class="paragraph">The standard chunk of Lorem Ipsum used since the 1500s is reproduced below for those interested. Sections 1.10.32 and 1.10.33 from "de Finibus Bonorum et Malorum" by Valerian are also reproduced in their exact original form, accompanied by English versions from the 1914 translation by H. Whitcombe.</p>
    </section>

    <div class="signature" role="img" aria-label="Handwritten signature of the sender"></div>
  </main>
</body>
</html>
```